Cross Country Transportation and Logistics Company need a Business Card Design

We need a business Card Design for a company based in Singapore, We had offices in Malaysia, Bangkok, Vietnam and China. Our Core business is cross border trucking to and from Singapore, Malaysia and Thailand. Our service also include event logistics, show moves and freight forwarding services. We made logistics possible is the region of Intra Asia.

Detail of the company as below.
Company Name: ORBEL FREIGHT (S) PTE LTD
Company Registration Number: 209847362K
Address: 48 Tenby Vale Industrial Park 3C #04-22 TVB Worksquare Singapore 583914
Office: +65 61847293
Fax: +65 61849376
Webiste: www.orbelfreight.com.sg

Business Card holder as below:
Name: Kevin Tan
Position: Director
Mobile: +65 9187 4063
Email: kevin.tan@orbelfreight.com.sg

Name: Melissa Koh
Position: Finance Manager
Mobile: +65 9472 8819
Email: melissa.koh@orbelfreight.com.sg

Name: Derek Soh
Position: General Manager
Mobile: +6012 846 3157
Email: derek.soh@orbelfreight.com.sg

Target Market(s)

I am targeting on the electronic component manufacturer and their freight to transport from Singapore to Malaysia and Thailand r vice verse.

Industry/Entity Type

Freight Forwarding

Requirements
Must have
• We make logistics possible

```html
<!DOCTYPE html>
<html lang="en">
<head>
<meta charset="UTF-8">
<title>Orbel Freight – Business Card</title>
<link href="https://fonts.googleapis.com/css2?family=Exo+2:wght@400;500;600&display=swap" rel="stylesheet">
<style>
  :root {
    --backdrop: #3a3a3c;
    --card: #f7f8fa;
    --ink: #2b2b30;
    --icon: #3d3f98;
    --rule: #1c82c4;
    --brand: #1d2f7a;
  }
  * { margin: 0; padding: 0; box-sizing: border-box; }
  html, body {
    width: 1200px; height: 816px; overflow: hidden;
    background: var(--backdrop);
    font-family: "Exo 2", sans-serif;
  }
  .card {
    position: absolute; left: 75px; top: 108px;
    width: 1050px; height: 600px;
    background: var(--card);
    border-radius: 44px;
    color: var(--ink);
  }
  .rule { position: absolute; height: 4px; background: var(--rule); }
  .rule--top { left: 150px; top: 140px; width: 420px; }
  .rule--bottom { left: 60px; top: 248px; width: 420px; }
  .icon {
    position: absolute; width: 44px; height: 44px; border-radius: 50%;
    background: var(--icon);
    display: flex; align-items: center; justify-content: center;
  }
  .icon svg { width: 24px; height: 24px; }
  .holder { position: absolute; left: 150px; top: 162px; }
  .holder__name { font-size: 27px; font-weight: 500; letter-spacing: 1.5px; line-height: 1.2; }
  .holder__role { font-size: 22px; letter-spacing: 2px; line-height: 1.3; }
  .icon--person { left: 85px; top: 176px; }
  .contact {
    position: absolute; left: 150px;
    font-size: 18px; letter-spacing: 1px; line-height: 1.35;
    white-space: nowrap;
  }
  .contact--phone { top: 292px; }
  .contact--web { top: 372px; }
  .contact--address { top: 452px; }
  .icon--phone { left: 90px; top: 295px; }
  .icon--web { left: 90px; top: 375px; }
  .icon--address { left: 90px; top: 466px; }
  .brand {
    position: absolute; left: 650px; top: 236px;
    color: var(--brand);
  }
  .brand__row {
    display: flex; align-items: center; gap: 16px;
    font-size: 40px; font-weight: 600; letter-spacing: 3px; line-height: 1.1;
  }
  .brand__dot { width: 28px; height: 28px; border-radius: 50%; background: var(--brand); flex: none; }
  .brand__tagline {
    margin-top: 10px; padding-left: 44px;
    font-size: 18px; font-weight: 500; letter-spacing: 2px; color: var(--rule);
  }
  .brand__reg {
    margin-top: 6px; padding-left: 44px;
    font-size: 14px; letter-spacing: 1.5px; color: var(--ink);
  }
</style>
</head>
<body>
  <div class="card">
    <div class="rule rule--top"></div>
    <div class="icon icon--person">
      <svg viewBox="0 0 24 24" fill="#fff"><circle cx="12" cy="8" r="4.5"/><path d="M3.5 21c0-4.7 3.8-7.5 8.5-7.5s8.5 2.8 8.5 7.5z"/></svg>
    </div>
    <div class="holder">
      <div class="holder__name">KEVIN TAN</div>
      <div class="holder__role">Director</div>
    </div>
    <div class="rule rule--bottom"></div>

    <div class="icon icon--phone">
      <svg viewBox="0 0 24 24" fill="none" stroke="#fff" stroke-width="2"><rect x="7" y="2.5" width="10" height="19" rx="2"/><line x1="11" y1="18" x2="13" y2="18"/></svg>
    </div>
    <div class="contact contact--phone">M +65 9187 4063<br>T +65 61847293&nbsp;&nbsp;F +65 61849376</div>

    <div class="icon icon--web">
      <svg viewBox="0 0 24 24" fill="none" stroke="#fff" stroke-width="2"><rect x="3" y="4" width="18" height="12" rx="1"/><line x1="12" y1="16" x2="12" y2="20"/><line x1="8" y1="20" x2="16" y2="20"/></svg>
    </div>
    <div class="contact contact--web">kevin.tan@orbelfreight.com.sg<br>www.orbelfreight.com.sg</div>

    <div class="icon icon--address">
      <svg viewBox="0 0 24 24" fill="#fff"><path d="M12 2a7 7 0 0 0-7 7c0 5 7 13 7 13s7-8 7-13a7 7 0 0 0-7-7zm0 9.5A2.5 2.5 0 1 1 12 6.5a2.5 2.5 0 0 1 0 5z"/></svg>
    </div>
    <div class="contact contact--address">48 Tenby Vale Industrial Park 3C<br>#04-22 TVB Worksquare<br>Singapore 583914</div>

    <div class="brand">
      <div class="brand__row">
        <span class="brand__dot"></span>
        <span class="brand__name">ORBEL FREIGHT</span>
      </div>
      <div class="brand__tagline">We make logistics possible</div>
      <div class="brand__reg">ORBEL FREIGHT (S) PTE LTD · 209847362K</div>
    </div>
  </div>
</body>
</html>
```